Power Point Template for Unique Indoor Advertising Company.

We need PowerPoint slide templates for our Sales Media Kit at our re-branded company based in Canada called "Bellwether Ad Collective".

Looking for a look that clearly and powerfully portrays our unique and effective indoor advertising billboards in our network.

Our Prime Billboards are strategically placed in high traffic areas of restaurants, pubs, nightclubs, fitness clubs, colleges and universities, and sports arenas.

Key features of our media is a captive audience and 100% gender specific.

You can visit our current website for info on our media (foxglovepromotions.ca)

Our Media Kits go out to small, medium business owners and advertising agenices and need to be eye-catching, trendy and slick.

Our logos are attached.

Deliverables are:

1) Presentation cover slide with rich graphic content and space for content.
2) Presentation body slide with room for content, 3-4 photos. This slide should have the following:
a) No graphic in the text area
b) Space for page number at the bottom.
3) Photoshop (PSD) files for all graphic elements.
4) Font files for all fonts used.

Target Market(s)

Advertising Agencies and Media Buyers

Industry/Entity Type

It Company

Font styles to use
Serif

Requirements
Must have
• Captivating and sleek look that is eye-catching and targeted.

```html
<!DOCTYPE html>
<html lang="en">
<head>
<meta charset="utf-8">
<title>Bellwether Ad Collective – Media Kit Slides</title>
<link rel="stylesheet" href="https://fonts.googleapis.com/css2?family=Open+Sans:wght@400;600;700&family=Arimo:wght@700&display=swap">
<style>
  :root {
    --band-blue: #4660f2;
    --page-white: #fbfbfd;
    --title-slate: #3e4a5c;
    --body-grey: #5f6166;
    --body-dark: #3b3c40;
    --teal-badge: #2ccf9c;
    --url-grey: #d3d6dd;
    --coin-blue: #1d8ccc;
    --tile-grey: #e9eaeb;
    --brick: #a98c6c;
    --brand-ink: #4a4d55;
  }
  * { margin: 0; padding: 0; box-sizing: border-box; }
  html, body { width: 973px; height: 1200px; overflow: hidden; background: var(--band-blue); }
  body { position: relative; font-family: "Open Sans", Arial, sans-serif; color: var(--body-grey); }

  .slide { position: absolute; left: 0; width: 973px; background: var(--page-white); overflow: hidden; }
  .slide--overview { top: 28px; height: 534px; }
  .slide--formats { top: 600px; height: 562px; }

  .page-badge {
    position: absolute; width: 28px; height: 28px; border-radius: 50%;
    background: var(--teal-badge); color: #fff; font-size: 11px;
    display: flex; align-items: center; justify-content: center;
  }

  .overview-title {
    position: absolute; top: 56px; left: 0; width: 973px; text-align: center;
    font-family: "Arimo", Arial, sans-serif; font-weight: 700; font-size: 27px;
    color: var(--title-slate);
  }

  .pillar-icon { position: absolute; top: 116px; }
  .pillar-funnel {
    position: absolute; left: 424px; top: 130px; width: 118px; height: 96px;
    border-radius: 10px;
    background: linear-gradient(180deg, #f9b12a 0%, #f7a21b 55%, #8cc63f 78%, #5ba8e6 100%);
  }
  .pillar-text { position: absolute; top: 250px; font-size: 15.5px; line-height: 21.5px; color: var(--body-grey); }
  .pillar-text ul { list-style: none; }
  .pillar-text li { position: relative; padding-left: 23px; }
  .pillar-text li::before { content: "•"; position: absolute; left: 0; font-size: 12px; }

  .brand-mark {
    position: absolute; display: flex; align-items: center; gap: 6px;
    font-size: 15px; font-weight: 600; color: var(--brand-ink);
  }
  .brand-mark .dot { width: 14px; height: 14px; border-radius: 50%; background: var(--brand-ink); }

  .site-url {
    position: absolute; right: 66px; top: 494px; font-size: 11px; font-weight: 700;
    letter-spacing: 0.5px; color: var(--url-grey);
  }

  .photo { position: absolute; }
  .photo--wallboard { left: 0; top: 0; width: 486px; height: 282px; background: linear-gradient(135deg, #f1f1f2, var(--tile-grey)); }
  .photo--wallboard .poster { position: absolute; left: 138px; top: 30px; width: 220px; height: 236px; background: #b9c3cc; border-radius: 2px; }
  .photo--wallboard .poster span { position: absolute; inset: 14px; background: linear-gradient(160deg, #5b2a7d, #7c4a96); }
  .photo--restroom { left: 490px; top: 282px; width: 483px; height: 280px; background: linear-gradient(180deg, var(--brick), #8f7458 90%, #5d5a58); }
  .photo--restroom .poster { position: absolute; left: 155px; top: 14px; width: 182px; height: 220px; background: #1f1f1f; }
  .photo--restroom .poster span { position: absolute; inset: 6px; background: #f9c322; }

  .divider { position: absolute; left: 486px; top: 0; width: 3px; height: 562px; background: var(--band-blue); }

  .format-block { position: absolute; font-size: 16px; line-height: 22.4px; color: var(--body-dark); }
  .format-block h2 { font-size: 16px; font-weight: 700; text-align: center; margin-bottom: 6px; }
  .format-block ul { list-style: none; }
  .format-block li { position: relative; color: var(--body-grey); }
  .format-block li::before { content: "•"; position: absolute; color: var(--body-grey); font-size: 12px; }
  .format-block p { color: var(--body-grey); }
  .format-block--wall { left: 35px; top: 286px; width: 420px; }
  .format-block--wall li { padding-left: 59px; }
  .format-block--wall li::before { left: 37px; }
  .format-block--prime { left: 511px; top: 14px; width: 460px; font-size: 15.5px; line-height: 22px; }
  .format-block--prime h2 { font-size: 16px; }
  .format-block--prime li { padding-left: 23px; }
  .format-block--prime li::before { left: 1px; }
  .nowrap { white-space: nowrap; }
</style>
</head>
<body>

<section class="slide slide--overview">
  <div class="page-badge" style="left:904px; top:28px;">5</div>
  <h1 class="overview-title">Bellwether Advertising Network</h1>

  <svg class="pillar-icon" style="left:150px;" width="130" height="118" viewBox="0 0 130 118" role="img" aria-label="Lightbulb sketch illustration inside a pentagon">
    <polygon points="65,2 128,46 104,116 26,116 2,46" fill="#d5dbe2" stroke="#9aa6b3" stroke-width="1"/>
  </svg>

  <div class="pillar-funnel" role="img" aria-label="Sales funnel illustration: traffic, leads, sales"></div>

  <svg class="pillar-icon" style="left:692px; top:128px;" width="106" height="106" viewBox="0 0 106 106" aria-hidden="true">
    <circle cx="52" cy="52" r="51" fill="var(--coin-blue)"/>
    <text x="36" y="68" text-anchor="middle" font-family="Arial, sans-serif" font-weight="700" font-size="44" fill="#fff">$</text>
    <polyline points="50,84 62,62 68,68 84,36" fill="none" stroke="#fff" stroke-width="5" stroke-linejoin="round"/>
    <polygon points="76,34 90,28 88,44" fill="#fff"/>
  </svg>

  <div class="pillar-text" style="left:112px; width:218px;">
    Innovative and effective indoor Prime Billboards and Wallboards strategically placed in high traffic areas of:
    <ul>
      <li>Restaurants,</li><li>Pubs,</li><li>Nightclubs,</li><li>Fitness Clubs,</li>
      <li>Colleges and Universities,</li><li>and Sports Arenas.</li>
    </ul>
  </div>
  <div class="pillar-text" style="left:385px; width:230px;">
    High impact branding placements at high traffic properties throughout British Columbia.
  </div>
  <div class="pillar-text" style="left:652px; width:220px;">
    Specializes in developing long-term revenue streams through the selling of sponsorship, supplier partnerships and naming rights packages.
  </div>

  <div class="brand-mark" style="left:50px; top:490px;"><span class="dot"></span>Bellwether Ad Collective</div>
  <div class="site-url">WWW.YOURDOMAIN.COM</div>
</section>

<section class="slide slide--formats">
  <div class="photo photo--wallboard" role="img" aria-label="Framed smoothie poster mounted on a white tiled wall"><div class="poster"><span></span></div></div>
  <div class="photo photo--restroom" role="img" aria-label="Yellow directory poster in a black frame on a brick wall"><div class="poster"><span></span></div></div>
  <div class="divider"></div>

  <div class="format-block format-block--prime">
    <h2>Prime Billboard</h2>
    <p>13" x 17" frames are strategically placed inside high traffic restrooms. Reaching consumers in a captive environment.</p>
    <p>Features</p>
    <ul>
      <li>100% Gender Specific (man/women)</li>
      <li>Guaranteed Readership</li>
      <li>Frequency</li>
      <li>Captive Audience</li>
      <li>Target Audience</li>
    </ul>
    <p>Networks</p>
    <ul>
      <li class="nowrap">Available in all 3 networks: <b>RestoBar</b>, <b>Sports</b>, and <b>Campus</b>.</li>
    </ul>
  </div>
  <div class="page-badge" style="left:930px; top:6px;">6</div>

  <div class="format-block format-block--wall">
    <h2>Wallboard</h2>
    <p>48" x 96" billboards are strategically placed on facility walls.</p>
    <p>Features</p>
    <ul>
      <li>Visible to all users of the facility</li>
      <li>High Impact &amp; Full Colour</li>
      <li>Increases Brand Awareness</li>
    </ul>
    <p>Networks</p>
    <ul>
      <li>Available in the <b>Sports</b> network</li>
    </ul>
  </div>

  <div class="brand-mark" style="left:50px; top:514px;"><span class="dot"></span>Bellwether Ad Collective</div>
</section>

</body>
</html>
```